property investment and development company needs a website

we need a website that looks professional and portrays trust for people looking to us to buy their house or investors looking to invest or joint venture with us.
We are based in the west midlands in the UK.
we deal mainly with residential housing, house to flats conversions, HMO's (houses in multiple ocupancy).
we require the website as a first point of contact with potential sellers, renters and investors so links or contact details that are easy to access or see would be good.
I have had logos designed by a brisk easel member and these can be used as guidance for the colour and style of the site.
Target Market(s)
joint venture investment partners, people looking to sell their house, people looking to rent from us.
Coding
Coded - Design and coding required
Number of Pages Required
3 page
Requirements
Must have
- project a professional appearance
- visable contact details

```html
<!DOCTYPE html>
<html lang="en">
<head>
<meta charset="utf-8">
<title>Halden Homes</title>
<link rel="stylesheet" href="https://fonts.googleapis.com/css2?family=Cinzel:wght@400;700&family=Lato:wght@400;700&display=swap">
<style>
:root{
  --gold:#c9a96e;
  --gold-dark:#b8955a;
  --charcoal:#333333;
  --ink:#222222;
  --white:#ffffff;
  --map:#c9c9c9;
  --navy:#1d2a4a;
}
*{margin:0;padding:0;box-sizing:border-box}
html,body{width:1200px;height:2673px;overflow:hidden}
body{position:relative;font-family:'Lato',sans-serif;color:var(--ink);background:var(--white)}
.abs{position:absolute}
.serif{font-family:'Cinzel',serif}

/* header */
.site-header{left:0;top:0;width:1200px;height:108px;background:var(--charcoal)}
.brand{left:118px;top:14px;display:flex;align-items:center;gap:14px}
.brand-mark{width:14px;height:14px;background:var(--gold)}
.brand-name{font-family:'Cinzel',serif;color:var(--white);font-size:36px;line-height:40px;letter-spacing:1px}
.main-nav{left:490px;top:46px;display:flex;align-items:center}
.main-nav a{font-family:'Cinzel',serif;color:var(--white);text-decoration:none;font-size:16px;letter-spacing:1px}
.main-nav a.active{color:var(--gold);border-bottom:2px solid var(--gold);padding-bottom:2px}
.main-nav .sep{width:1px;height:16px;background:#666;margin:0 34px}

/* hero */
.hero{left:0;top:108px;width:1200px;height:621px;background:linear-gradient(160deg,#8d95a8 0%,#4c5468 45%,#2a3044 100%)}
.hero-title{left:0;top:262px;width:1200px;text-align:center;color:var(--white);font-family:'Cinzel',serif;font-size:36px;line-height:49px;letter-spacing:1px;text-shadow:0 2px 6px rgba(0,0,0,.5)}
.hero-dots{left:560px;top:588px;display:flex;gap:9px}
.hero-dots span{width:13px;height:13px;border-radius:50%;border:1.5px solid var(--white)}
.hero-dots span.on{background:var(--gold);border-color:var(--gold)}

/* about */
.about-emblem{left:125px;top:838px;width:290px;height:324px;display:flex;align-items:center;justify-content:center}
.about-emblem span{font-family:'Cinzel',serif;color:var(--gold);font-size:40px;line-height:48px;text-align:center}
.about-rule{left:458px;top:850px;width:2px;height:300px;background:#d5d5d5}
.about-title{left:499px;top:876px;font-family:'Cinzel',serif;font-size:30px;color:var(--ink);letter-spacing:1px}
.about-copy{left:499px;top:941px;width:580px;font-size:12px;line-height:17px;color:#333}
.about-copy p{margin-bottom:13px}
.btn-outline{left:498px;top:1063px;width:158px;height:37px;border:1px solid var(--gold);border-radius:20px;color:var(--gold);font-weight:700;font-size:14px;display:flex;align-items:center;justify-content:center}

/* panels */
.panel{top:1258px;width:600px;height:540px}
.panel-invest{left:0;background:linear-gradient(135deg,#d8bd86 0%,#c7a76a 55%,#a88a55 100%)}
.panel-sell{left:600px;background:linear-gradient(135deg,#2b3b66 0%,var(--navy) 50%,#3a3f48 100%)}
.panel-inner{position:absolute;left:0;top:0;width:600px;text-align:center;color:var(--white)}
.panel-title{margin-top:94px;font-family:'Cinzel',serif;font-size:30px;letter-spacing:1px}
.panel-rule{width:52px;height:2px;background:var(--white);margin:9px auto 0}
.panel-sell .panel-title{color:var(--gold)}
.panel-sell .panel-rule{background:var(--gold)}
.panel-copy{width:440px;margin:35px auto 0;font-size:12px;line-height:20px}
.panel-copy p{margin-bottom:21px}
.panel-copy strong{font-size:15px}
.pill{display:inline-flex;align-items:center;justify-content:center;height:38px;border-radius:20px;font-weight:700;font-size:15px;color:var(--white);padding:0 22px}
.pill-dark{background:#3a3835;color:var(--gold)}
.pill-gold{background:var(--gold)}

/* subscribe */
.cta-title{left:120px;top:1896px;font-family:'Cinzel',serif;font-size:27px;color:var(--gold);letter-spacing:1px}
.cta-sub{left:120px;top:1929px;font-size:16px;font-weight:700;color:var(--ink)}
.subscribe{left:550px;top:1896px;width:530px;height:54px;border:1px solid #d5d5d5;border-radius:28px}
.subscribe-field{left:12px;top:18px;font-size:11px;color:#888}
.subscribe-btn{right:-1px;top:-1px;width:178px;height:54px;border-radius:28px;background:var(--gold);color:var(--white);font-weight:700;font-size:17px;display:flex;align-items:center;justify-content:center}

/* contact */
.map{left:0;top:2048px;width:1200px;height:482px;background:linear-gradient(160deg,#d4d4d4,#bdbdbd)}
.details{left:189px;top:2272px;width:422px;height:165px;background:rgba(40,40,40,.88);padding:22px 23px;color:var(--white)}
.details h3{font-family:'Cinzel',serif;font-weight:400;color:var(--gold);font-size:16px;letter-spacing:1px;margin-bottom:10px}
.details li{list-style:none;display:flex;align-items:center;gap:11px;font-size:14px;line-height:26px}
.details svg{width:14px;height:14px;flex:none}
.form-card{left:596px;top:2137px;width:484px;height:323px;background:var(--white);padding:30px 34px}
.form-card h2{font-family:'Cinzel',serif;font-weight:400;color:var(--gold);font-size:25px;letter-spacing:1px;margin-bottom:14px}
.field{border:1px solid #cfcfcf;height:38px;font-size:11px;color:#777;padding:12px 8px}
.field-row{display:flex;gap:10px;margin-bottom:9px}
.field-row .field{width:203px}
.field-area{height:90px;margin-bottom:10px}

/* footer */
.site-footer{left:0;top:2530px;width:1200px;height:143px;background:var(--charcoal);color:var(--white)}
.foot-nav{left:118px;top:48px;display:flex;align-items:center;font-size:12px}
.foot-nav .sep{width:1px;height:14px;background:#666;margin:0 40px}
.copyright{left:118px;top:83px;font-size:11px}
.follow{left:924px;top:40px;font-size:20px;font-weight:700;color:var(--gold)}
.socials{left:923px;top:75px;display:flex;gap:13px}
.socials span{width:30px;height:30px;border-radius:50%;background:var(--white)}
.socials span:first-child{background:var(--gold)}
</style>
</head>
<body>

<header class="site-header abs">
  <div class="brand abs"><span class="brand-mark"></span><span class="brand-name">Halden<br>Homes</span></div>
  <nav class="main-nav abs">
    <a class="active" href="#">Home</a><span class="sep"></span>
    <a href="#">About Us</a><span class="sep"></span>
    <a href="#">Invest</a><span class="sep"></span>
    <a href="#">Sell</a><span class="sep"></span>
    <a href="#">Contact Us</a>
  </nav>
</header>

<section class="hero abs" role="img" aria-label="Looking up at glass office towers against a cloudy sky">
  <h1 class="hero-title abs" style="font-weight:400">We are a property development and<br>investment company</h1>
  <div class="hero-dots abs"><span class="on"></span><span></span><span></span><span></span></div>
</section>

<section class="about">
  <div class="about-emblem abs"><span>Halden<br>Homes</span></div>
  <div class="about-rule abs"></div>
  <h2 class="about-title abs" style="font-weight:400">About Halden Homes</h2>
  <div class="about-copy abs">
    <p>Weare a property development and investment company that have our own portfolio and we are active investorswho pride ourselves in expanding our business organically.</p>
    <p>We ensure that whatever your property needs are we deliver bespoke services for our clients. For investors, sellers, landlords and tenants we bring knowledge to your next property decision, allowing you to make an informed decision.</p>
  </div>
  <div class="btn-outline abs">READ MORE ››</div>
</section>

<section class="panel panel-invest abs" role="img" aria-label="Residential houses at sunset with a warm gold tint">
  <div class="panel-inner">
    <h2 class="panel-title" style="font-weight:400">Invest</h2>
    <div class="panel-rule"></div>
    <div class="panel-copy">
      <p>We have our own portfolio and we are active investors, so our finger is on the pulse and we are currently looking for residential development investments &amp; commercial to residential conversions in cities or regional centres showing strong growth.</p>
      <p>Our experience in the industry enables us to make extremely quick andwell-informed decisions. We follow the opportunities that are presented to us as well as sourcing opportunities ourselves.We are happy to work in partnership and within joint ventures and have a proven track record of establishing excellent relationships in these areas.</p>
    </div>
    <span class="pill pill-dark">READ MORE ››</span>
  </div>
</section>

<section class="panel panel-sell abs" role="img" aria-label="A hand holding house keys in front of a family home">
  <div class="panel-inner">
    <h2 class="panel-title" style="font-weight:400">Sell</h2>
    <div class="panel-rule"></div>
    <div class="panel-copy" style="width:450px">
      <p>We undertake the necessary market research to evaluate an option that works for all parties involved. We will help guide you to make an informed decision on how to gain the maximum realistic value.</p>
      <p>For those looking to achieve a fast and professional sale to experienced investors, we provide an approach that has been proven to work for many others.</p>
      <p>If you would like to discuss a property you are looking to sell,<br>then please contact us on <strong>01632 960418</strong></p>
    </div>
    <span class="pill pill-gold" style="margin-top:-8px">CALL US TODAY ››</span>
  </div>
</section>

<section class="cta">
  <h2 class="cta-title abs" style="font-weight:400">Are you invest or selling?</h2>
  <p class="cta-sub abs">SEARCH YOUR DREAM HOME</p>
  <div class="subscribe abs">
    <span class="subscribe-field abs">your email adddress</span>
    <span class="subscribe-btn abs">SUBSCRIBE NOW</span>
  </div>
</section>

<section class="contact">
  <div class="map abs" role="img" aria-label="Street map of the area around the office"></div>
  <div class="details abs">
    <h3>Company Detalis</h3>
    <ul>
      <li><svg viewBox="0 0 16 16"><path fill="#c9a96e" d="M3 1l3 3-2 2c1 2 3 4 5 5l2-2 3 3-2 3C7 15 1 9 1 3z"/></svg>01632 960418</li>
      <li><svg viewBox="0 0 16 16"><path fill="#c9a96e" d="M3 1l3 3-2 2c1 2 3 4 5 5l2-2 3 3-2 3C7 15 1 9 1 3z"/></svg>07700 900231</li>
      <li><svg viewBox="0 0 16 16"><rect x="1" y="3" width="14" height="10" fill="#c9a96e"/><path d="M1 3l7 6 7-6" stroke="#333" fill="none"/></svg>info@haldenhomes.co.uk</li>
      <li><svg viewBox="0 0 16 16"><path d="M8 15S3 9 3 6a5 5 0 0110 0c0 3-5 9-5 9z" fill="none" stroke="#c9a96e" stroke-width="1.5"/><circle cx="8" cy="6" r="1.8" fill="#c9a96e"/></svg>12 Ashby Lane, Fernbridge, Westshire, FB4 2LQ</li>
    </ul>
  </div>
  <div class="form-card abs">
    <h2>Contact Us</h2>
    <div class="field-row"><div class="field">Your Name</div><div class="field">Your Email</div></div>
    <div class="field-row"><div class="field">Your Phone</div><div class="field">Subject</div></div>
    <div class="field field-area">Your Message</div>
    <span class="pill pill-gold" style="font-size:16px">SEND MESSAGE ››</span>
  </div>
</section>

<footer class="site-footer abs">
  <nav class="foot-nav abs">
    <span>HOME</span><span class="sep"></span>
    <span>ABOUT US</span><span class="sep"></span>
    <span>INVEST</span><span class="sep"></span>
    <span>SELL</span><span class="sep"></span>
    <span>CONTACT US</span>
  </nav>
  <p class="copyright abs">Copyright © 2019 HALDEN HOMES. All Right Reserved</p>
  <p class="follow abs">Follow Us On :</p>
  <div class="socials abs"><span></span><span></span><span></span><span></span></div>
</footer>

</body>
</html>
```